Brightfield Co Trade Show Flyer

We need a brochure design (8.5 x 11) Info in the design (refer to rough draft I drew on Paper): "#1 selling tool to aquire new franchisees has been video testimonials" - Martin L. Crowe, C.E.O Tovik Smoothie Franchise Testimonials - Let your franchisees do the selling for you. Franchisee testimonial: $10,000 / per Franchisee Includes: • 2 minute Video • 1 minute add for your franchise's location • Concept creation • Communication with franchisee • Travel to their location • All rental equipment • 1 round of corrections • Animated logo • Licensed music ******* For 25% Discount section (next to middle box), please put the "Outlet Summit Logo" Great to use on all your social media (USE logos and icons) • Website • Video • Jobs • Social • Photo • Posts • Phone calls • Emails • In person meetings Some of our clients: (use the logos I uploaded - in round boxes as in draft) LOGO (Brightfield Franchise Testimonial) www.brightfieldvoices.example (866) 555-0172

Target Market(s)

Franchise owners

Colors

Designer to choose colors to be used in the design.

Requirements

```html
<!DOCTYPE html>
<html lang="en">
<head>
<meta charset="utf-8">
<title>Brightfield Co – Franchise Testimonials Flyer</title>
<link href="https://fonts.googleapis.com/css2?family=Arimo:wght@400;700&family=Open+Sans:wght@700;800&family=Oswald:wght@500;600;700&display=swap" rel="stylesheet">
<style>
  :root{
    --navy:#0a1a7c;
    --navy-deep:#0b1560;
    --hero-mid:#1a2f9e;
    --orange:#ff9e0c;
    --white:#ffffff;
    --ink:#1b1f3a;
    --grey-panel:#d9dfdc;
    --expo-green:#2fd862;
    --dash:#555b6e;
  }
  *{box-sizing:border-box;margin:0;padding:0}
  html,body{width:927px;height:1200px;overflow:hidden;background:var(--white)}
  .flyer{position:relative;width:927px;height:1200px;overflow:hidden;font-family:"Arimo",Arial,sans-serif;color:var(--ink)}

  .hero{position:absolute;left:0;top:0;width:927px;height:408px;
    background:radial-gradient(ellipse at 55% 55%, var(--hero-mid) 0%, var(--navy) 55%, var(--navy-deep) 100%);color:var(--white);text-align:center}
  .hero-quote-mark{position:absolute;left:0;right:0;top:28px;font-family:"Open Sans",sans-serif;font-weight:800;font-size:120px;line-height:1}
  .hero-quote{position:absolute;left:0;right:0;top:120px;font-size:24px}
  .hero-attribution{position:absolute;right:100px;top:156px;font-size:15.5px}
  .hero-title{position:absolute;left:0;right:0;top:228px;font-family:"Open Sans",sans-serif;font-weight:800;color:var(--orange);font-size:60px;line-height:54px;letter-spacing:-0.5px}
  .hero-tagline{position:absolute;left:0;right:0;top:350px;font-size:24.5px;letter-spacing:0.2px}

  .includes{position:absolute;top:432px;list-style:none;font-size:16.5px;color:#222;line-height:1.15}
  .includes li{position:relative;padding-left:24px;margin-bottom:5px}
  .includes svg{position:absolute;left:0;top:-4px}
  .includes--left{left:42px}
  .includes--right{left:590px}
  .includes--right li{margin-bottom:5.5px}

  .discount{position:absolute;left:146px;top:576px;font-family:"Oswald",sans-serif;font-weight:700;font-size:88px;line-height:1;color:var(--navy);letter-spacing:-1px;white-space:nowrap;transform:scaleX(0.82);transform-origin:left top}
  .discount-for{position:absolute;left:604px;top:612px;font-family:"Oswald",sans-serif;font-weight:700;font-size:24px;line-height:1;color:var(--navy);transform:rotate(-90deg);transform-origin:center}
  .summit{position:absolute;left:642px;top:598px;display:flex;align-items:center;gap:8px}
  .summit-square{width:26px;height:26px;background:var(--expo-green);flex:none}
  .summit-name{font-family:"Arimo",sans-serif;font-weight:700;font-size:21px;color:var(--expo-green);line-height:1.05;width:100px}

  .channels{position:absolute;left:67px;top:702px;width:786px;height:152px;border:1.5px dashed var(--dash)}
  .channels-title{position:absolute;left:50%;top:-15px;transform:translateX(-50%);background:var(--white);padding:0 22px;font-size:22px;font-weight:400;white-space:nowrap;color:#222}
  .channel{position:absolute;top:40px;width:75px;height:75px;border-radius:50%;background:var(--navy);color:var(--white);display:flex;align-items:center;justify-content:center;font-weight:700;font-size:12px;letter-spacing:0.5px}

  .trusted{position:absolute;left:0;right:0;top:872px;text-align:center;font-family:"Oswald",sans-serif;font-weight:700;font-size:38px;color:var(--navy);transform:scaleX(0.82)}
  .client{position:absolute;top:942px;height:56px;display:flex;align-items:center;justify-content:center;text-align:center;font-weight:700;font-size:12px;line-height:1.15;color:var(--navy)}
  .client-dot{width:14px;height:14px;border-radius:50%;background:var(--orange);margin-right:5px;flex:none}

  .footer{position:absolute;left:0;top:1000px}
  .footer-brand{position:absolute;left:40px;top:1110px;display:flex;align-items:center;gap:10px;color:var(--white)}
  .footer-brand-mark{width:30px;height:30px;border-radius:50%;background:var(--white);flex:none}
  .footer-brand-name{font-family:"Open Sans",sans-serif;font-weight:800;font-size:28px;line-height:1;white-space:nowrap}
  .footer-phone{position:absolute;left:645px;top:1034px;font-family:"Oswald",sans-serif;font-weight:700;font-size:44px;line-height:1;color:var(--navy);white-space:nowrap;transform:scaleX(0.82);transform-origin:left top;letter-spacing:0.5px}
  .footer-contact{position:absolute;right:42px;top:1138px;font-size:19.5px;color:var(--white);white-space:nowrap}
  .footer-contact span{margin:0 14px}
</style>
</head>
<body>
<div class="flyer">

  <section class="hero" role="img" aria-label="Photo of a person in a suit signing a document, tinted deep blue">
    <div class="hero-quote-mark">&ldquo;</div>
    <p class="hero-quote">#1 selling tool to aquire new franchisees has been video testimonials"</p>
    <p class="hero-attribution">- MARTIN L. CROWE, C.E.O</p>
    <h1 class="hero-title">FRANCHISE<br>TESTIMONIALS</h1>
    <p class="hero-tagline">LET YOUR FRANCHISEES DO THE SELLING FOR YOU.</p>
  </section>

  <ul class="includes includes--left">
    <li><svg width="22" height="22" viewBox="0 0 22 22"><rect x="1" y="6" width="14" height="14" fill="none" stroke="#0a1a7c" stroke-width="1.8"/><path d="M4 12 L8 17 L20 1" fill="none" stroke="#ff9e0c" stroke-width="2.6"/></svg>FRANCHISEE TESTIMONIAL: $10,000 /<br>PER FRANCHISEE INCLUDES 2 MINUTE VIDEO</li>
    <li><svg width="22" height="22" viewBox="0 0 22 22"><rect x="1" y="6" width="14" height="14" fill="none" stroke="#0a1a7c" stroke-width="1.8"/><path d="M4 12 L8 17 L20 1" fill="none" stroke="#ff9e0c" stroke-width="2.6"/></svg>1 MINUTE ADD FOR YOUR FRANCHISE'S LOCATION</li>
    <li><svg width="22" height="22" viewBox="0 0 22 22"><rect x="1" y="6" width="14" height="14" fill="none" stroke="#0a1a7c" stroke-width="1.8"/><path d="M4 12 L8 17 L20 1" fill="none" stroke="#ff9e0c" stroke-width="2.6"/></svg>CONCEPT CREATION</li>
    <li><svg width="22" height="22" viewBox="0 0 22 22"><rect x="1" y="6" width="14" height="14" fill="none" stroke="#0a1a7c" stroke-width="1.8"/><path d="M4 12 L8 17 L20 1" fill="none" stroke="#ff9e0c" stroke-width="2.6"/></svg>COMMUNICATION WITH FRANCHISEE</li>
  </ul>
  <ul class="includes includes--right">
    <li><svg width="22" height="22" viewBox="0 0 22 22"><rect x="1" y="6" width="14" height="14" fill="none" stroke="#0a1a7c" stroke-width="1.8"/><path d="M4 12 L8 17 L20 1" fill="none" stroke="#ff9e0c" stroke-width="2.6"/></svg>TRAVEL TO THEIR LOCATION</li>
    <li><svg width="22" height="22" viewBox="0 0 22 22"><rect x="1" y="6" width="14" height="14" fill="none" stroke="#0a1a7c" stroke-width="1.8"/><path d="M4 12 L8 17 L20 1" fill="none" stroke="#ff9e0c" stroke-width="2.6"/></svg>ALL RENTAL EQUIPMENT</li>
    <li><svg width="22" height="22" viewBox="0 0 22 22"><rect x="1" y="6" width="14" height="14" fill="none" stroke="#0a1a7c" stroke-width="1.8"/><path d="M4 12 L8 17 L20 1" fill="none" stroke="#ff9e0c" stroke-width="2.6"/></svg>1 ROUND OF CORRECTIONS</li>
    <li><svg width="22" height="22" viewBox="0 0 22 22"><rect x="1" y="6" width="14" height="14" fill="none" stroke="#0a1a7c" stroke-width="1.8"/><path d="M4 12 L8 17 L20 1" fill="none" stroke="#ff9e0c" stroke-width="2.6"/></svg>ANIMATED LOGO</li>
    <li><svg width="22" height="22" viewBox="0 0 22 22"><rect x="1" y="6" width="14" height="14" fill="none" stroke="#0a1a7c" stroke-width="1.8"/><path d="M4 12 L8 17 L20 1" fill="none" stroke="#ff9e0c" stroke-width="2.6"/></svg>LICENSED MUSIC</li>
  </ul>

  <div class="discount">25% DISCOUNT</div>
  <div class="discount-for">FOR</div>
  <div class="summit">
    <div class="summit-square"></div>
    <div class="summit-name">Outlet Summit</div>
  </div>

  <section class="channels">
    <h2 class="channels-title">USE YOUR TESTIMONIALS EVERYWHERE</h2>
    <div class="channel" style="left:45px">WEB</div>
    <div class="channel" style="left:134px">VIDEO</div>
    <div class="channel" style="left:224px">JOBS</div>
    <div class="channel" style="left:315px">SOCIAL</div>
    <div class="channel" style="left:402px">PHOTO</div>
    <div class="channel" style="left:492px">POSTS</div>
    <div class="channel" style="left:582px">
      <svg width="44" height="44" viewBox="0 0 44 44" fill="none" stroke="#fff" stroke-width="2.4"><circle cx="22" cy="22" r="19"/><path d="M15 12 l4 -1 l3 6 l-3 2 q2 5 7 7 l2 -3 l6 3 l-1 4 q-4 3 -11 -2 q-7 -6 -7 -16z" fill="#fff" stroke="none"/></svg>
    </div>
    <div class="channel" style="left:673px">
      <svg width="40" height="36" viewBox="0 0 40 36" fill="none" stroke="#fff" stroke-width="2.6"><rect x="2" y="10" width="36" height="24"/><path d="M2 10 L20 24 L38 10"/><path d="M8 10 V2 H32 V10"/></svg>
    </div>
  </section>

  <h2 class="trusted">- TRUSTED BY -</h2>
  <div class="client" style="left:246px;width:88px"><span class="client-dot"></span>Cobbleton Creamery</div>
  <div class="client" style="left:340px;width:80px">Quickstop Nine</div>
  <div class="client" style="left:418px;width:88px">Tovik Smoothie</div>
  <div class="client" style="left:512px;width:76px">Tidewell Cleaning</div>
  <div class="client" style="left:598px;width:86px">Rotary Auto Care</div>

  <svg class="footer" width="927" height="200" viewBox="0 0 927 200">
    <polygon points="0,1 215,1 280,78 927,78 927,200 0,200" fill="#0a1a7c"/>
    <polygon points="268,67 540,67 531,78 280,78" fill="#ff9e0c"/>
    <polygon points="563,25 927,25 927,106 514,106" fill="#d9dfdc"/>
    <circle cx="610" cy="63" r="18" fill="none" stroke="#0a1a7c" stroke-width="3"/>
    <path d="M601 53 l4 -1 l3 6 l-3 2 q2 5 7 7 l2 -3 l6 3 l-1 4 q-4 3 -11 -2 q-7 -6 -7 -16z" fill="#0a1a7c"/>
  </svg>
  <div class="footer-brand"><span class="footer-brand-mark"></span><span class="footer-brand-name">Brightfield Co</span></div>
  <div class="footer-phone">(866) 555-0172</div>
  <p class="footer-contact">www.brightfieldvoices.example<span>|</span>hello@brightfieldvoices.example</p>

</div>
</body>
</html>
```